Business Card for TQB Field Services

Would like a large logo on one side. On the other side, logo on one side and company phone number, address, and email on the other side. I don't have a logo so please create one for us.
Updates
I don't have a logo, so please create one for us.
Target Market(s)
Land Surveying
Industry/Entity Type
Surveyor
Contact Information for Business Card
Would like a large logo on one side. On the other side, logo on one side and company phone number, address, and email on the other side
Requirements
Nice to have
- would like the initials to be incorporated with the logo

```html
<!DOCTYPE html>
<html lang="en">
<head>
<meta charset="utf-8">
<title>TQB Field Services – Business Card</title>
<link href="https://fonts.googleapis.com/css2?family=Open+Sans:wght@400;600&display=swap" rel="stylesheet">
<style>
  :root {
    --bg: #e9e9ea;
    --card: #ffffff;
    --ink: #1b1b1b;
    --purple: #7a2a97;
    --band: #050505;
  }
  * { box-sizing: border-box; margin: 0; padding: 0; }
  html, body { width: 1200px; height: 903px; overflow: hidden; }
  body {
    background: var(--bg);
    font-family: "Open Sans", sans-serif;
    color: var(--ink);
    position: relative;
  }
  .card {
    position: absolute;
    top: 297px;
    width: 540px;
    height: 309px;
    background: var(--card);
    box-shadow: 0 4px 14px rgba(0,0,0,.12);
    overflow: hidden;
  }
  .card--front { left: 40px; }
  .card--back { left: 620px; }

  /* Front */
  .band { position: absolute; left: 0; right: 0; height: 30px; background: var(--band); }
  .band--top { top: 0; }
  .band--bottom { bottom: 0; }
  .holder { position: absolute; left: 30px; top: 44px; line-height: 1.15; }
  .holder__name { color: var(--purple); font-size: 21px; letter-spacing: .5px; }
  .holder__title { font-size: 17px; }
  .brand {
    position: absolute;
    display: flex;
    align-items: center;
    gap: 14px;
  }
  .brand__mark {
    border: 1.5px solid var(--ink);
    border-radius: 50%;
  }
  .brand__name { color: var(--purple); font-weight: 400; white-space: nowrap; }
  .card--front .brand { left: 112px; top: 122px; }
  .card--front .brand__mark { width: 78px; height: 78px; }
  .card--front .brand__name { font-size: 32px; }

  /* Back */
  .card--back .brand__name {
    position: absolute; right: 30px; top: 26px; font-size: 30px;
  }
  .contacts { position: absolute; left: 28px; top: 32px; list-style: none; font-size: 13px; line-height: 19px; }
  .contacts li { display: flex; align-items: center; gap: 8px; }
  .contacts svg { width: 12px; height: 12px; flex: none; }
  .rule {
    position: absolute; left: 48px; top: 116px; width: 345px;
    border-top: 1.5px solid var(--purple);
  }
  .target {
    position: absolute; left: 393px; top: 170px;
    width: 100px; height: 100px;
    border: 1.5px solid var(--purple); border-radius: 50%;
  }
  .target-stem {
    position: absolute; left: 393px; top: 116px; width: 0; height: 0;
  }
  .address { position: absolute; left: 28px; top: 128px; display: flex; gap: 8px; font-size: 11.5px; line-height: 16px; }
  .address svg { width: 12px; height: 14px; flex: none; margin-top: 1px; }
</style>
</head>
<body>

<section class="card card--front" aria-label="Business card front">
  <div class="band band--top"></div>
  <div class="holder">
    <p class="holder__name">Your Name</p>
    <p class="holder__title">Job Title</p>
  </div>
  <div class="brand">
    <span class="brand__mark"></span>
    <span class="brand__name">TQB Field Services</span>
  </div>
  <div class="band band--bottom"></div>
</section>

<section class="card card--back" aria-label="Business card back">
  <ul class="contacts">
    <li><svg viewBox="0 0 12 12"><path d="M2.5 1l2 2.5-1 1.2c.7 1.4 1.6 2.3 3 3l1.2-1 2.5 2-1 1.8C5.5 10.2 1.8 6.5 1 2z" fill="var(--purple)"/></svg>202 3030</li>
    <li><svg viewBox="0 0 12 12"><rect x="3" y="0.5" width="6" height="11" rx="1" fill="none" stroke="var(--purple)" stroke-width="1.2"/></svg>0987654321</li>
    <li><svg viewBox="0 0 12 12"><g fill="none" stroke="var(--purple)" stroke-width="1"><circle cx="6" cy="6" r="5"/><ellipse cx="6" cy="6" rx="2.2" ry="5"/><path d="M1 6h10M2 3.3h8M2 8.7h8"/></g></svg>www.TQB Field Services.co.nz</li>
    <li><svg viewBox="0 0 12 12"><rect x="0.5" y="2" width="11" height="8" fill="var(--purple)"/><path d="M0.5 2l5.5 4.5L11.5 2" fill="none" stroke="#fff" stroke-width="1"/></svg>services@fieldmail.co.nz</li>
  </ul>
  <div class="rule"></div>
  <svg class="target-stem" width="1" height="1" style="overflow:visible" aria-hidden="true"><line x1="0" y1="0" x2="30" y2="56" stroke="var(--purple)" stroke-width="1.5"/></svg>
  <div class="address">
    <svg viewBox="0 0 12 14"><path d="M6 0a5 5 0 0 0-5 5c0 3.5 5 9 5 9s5-5.5 5-9a5 5 0 0 0-5-5zm0 7a2 2 0 1 1 0-4 2 2 0 0 1 0 4z" fill="var(--purple)"/></svg>
    <p>TQB Field Services<br>First Floor, 27 Kowhai Street, Riverton<br>PO Box 512 480, Westhaven Auckland</p>
  </div>
  <div class="target"></div>
  <div class="brand"><span class="brand__name">TQB Field Services</span></div>
</section>

</body>
</html>
```